Frozen Yoghurt
Aufgabenstellung
Es soll eine Postkarte erstellt werden
auf die Vorteile des Produkts dargestellt werden
- kein fett (98% fettfrei)
- keine künstlichen süssungsmittel
- low calorien
- Viel Calcium
- Viel Eiweiss
- Vitamine durch Frucht topping
Die Postkarte soll gleichzeitig dazu dienen dass man sie mit zu uns ins Geschäft bringt und dann ein gratis Muster bekommt.
Mitbewerber: www.plumdrizzle.com, www.velvocup.com

```html
<!DOCTYPE html>
<html lang="de">
<head>
<meta charset="utf-8">
<title>Frozen Yoghurt – Postkarte</title>
<link href="https://fonts.googleapis.com/css2?family=Nunito:ital,wght@0,400;0,600;0,700;0,800;1,400;1,800;1,900&display=swap" rel="stylesheet">
<style>
  :root {
    --green-deep: #3f9a16;
    --green-main: #6cbb25;
    --green-light: #b6dc6a;
    --green-pale: #e3f2c4;
    --green-text: #7ab51d;
    --red: #d5141f;
    --white: #ffffff;
    --grey-line: #9a9a9a;
    --text-dark: #333333;
  }
  * { box-sizing: border-box; margin: 0; padding: 0; }
  html, body { width: 850px; height: 1200px; overflow: hidden; background: var(--white); }
  body { position: relative; font-family: "Nunito", sans-serif; }

  .card { position: absolute; left: 17px; width: 816px; overflow: hidden; }

  /* Front side */
  .card--front {
    top: 17px; height: 574px;
    background: radial-gradient(ellipse at 70% 35%, var(--green-light) 0%, var(--green-main) 45%, var(--green-deep) 100%);
  }
  .front__swoosh { position: absolute; inset: 0; }
  .front__title {
    position: absolute; left: 72px; top: 50px;
    color: var(--white); font-weight: 900; font-style: italic;
    line-height: 0.95; transform: rotate(-7deg); transform-origin: left top;
    text-shadow: 2px 3px 4px rgba(0,0,0,0.25);
  }
  .front__title .line-1 { display: block; font-size: 74px; }
  .front__title .line-2 { display: block; font-size: 86px; padding-left: 6px; }
  .front__tagline {
    position: absolute; left: 92px; top: 262px;
    color: var(--white); font-size: 28px; font-weight: 600; font-style: italic;
    line-height: 1.25; transform: rotate(-7deg); transform-origin: left top;
  }
  .front__product {
    position: absolute; left: 460px; top: 190px; width: 350px; height: 360px;
    border-radius: 48% 48% 40% 40%;
    background: radial-gradient(ellipse at 50% 40%, #f5f0dc 0%, #e9d5a8 35%, #b5323a 70%, rgba(150,200,90,0) 100%);
  }
  .front__offer {
    position: absolute; left: 28px; top: 458px;
    color: var(--red); font-size: 17px; font-weight: 700;
    transform: rotate(9deg); transform-origin: left top; white-space: nowrap;
  }
  .front__offer strong { font-weight: 900; }

  /* Back side */
  .card--back {
    top: 607px; height: 576px;
    background: var(--white); border: 1px solid #d6d6d6;
  }
  .back__swoosh { position: absolute; inset: 0; }
  .back__title {
    position: absolute; left: 64px; top: 54px;
    color: var(--green-text); font-weight: 900; font-style: italic;
    line-height: 0.95; transform: rotate(-5deg); transform-origin: left top;
  }
  .back__title .line-1 { display: block; font-size: 44px; }
  .back__title .line-2 { display: block; font-size: 52px; padding-left: 2px; }
  .benefits { position: absolute; left: 64px; top: 212px; width: 360px; color: var(--green-text); }
  .benefits__lead { font-size: 20px; font-weight: 700; line-height: 1.2; margin-bottom: 22px; }
  .benefits__list { list-style: none; }
  .benefits__list li {
    position: relative; padding-left: 16px; font-size: 18px; font-weight: 600;
    line-height: 1.25; margin-bottom: 16px;
  }
  .benefits__list li::before {
    content: ""; position: absolute; left: 0; top: 8px; width: 8px; height: 8px;
    border: 1.5px solid var(--green-text); border-radius: 50%;
  }
  .voucher {
    position: absolute; left: 64px; top: 488px;
    color: var(--red); font-size: 16px; font-weight: 600; line-height: 1.35;
  }
  .voucher strong { font-weight: 800; }
  .divider { position: absolute; left: 429px; top: 221px; width: 1px; height: 304px; background: #c8c8c8; }
  .brand {
    position: absolute; left: 596px; top: 64px;
    display: flex; align-items: center; gap: 8px;
    color: var(--green-deep); font-size: 20px; font-weight: 800;
  }
  .brand__mark { width: 14px; height: 14px; background: var(--red); }
  .address { position: absolute; left: 484px; top: 286px; width: 278px; }
  .address__intro { color: var(--green-text); font-size: 16px; font-weight: 600; margin-bottom: 14px; }
  .address__line {
    font-size: 18px; font-style: italic; color: var(--text-dark);
    border-bottom: 1px solid var(--grey-line); padding: 4px 0 2px; margin-bottom: 16px;
  }
  .address__closing { color: var(--red); font-size: 16px; font-weight: 800; margin-top: 4px; }
</style>
</head>
<body>

<section class="card card--front">
  <svg class="front__swoosh" viewBox="0 0 816 574" width="816" height="574" aria-hidden="true">
    <path d="M0 400 C 250 430, 500 560, 816 520 L816 574 L0 574 Z" fill="var(--green-pale)" opacity="0.7"/>
    <path d="M0 440 C 260 460, 520 590, 816 530" fill="none" stroke="var(--red)" stroke-width="7"/>
    <path d="M0 455 C 260 478, 520 600, 816 545" fill="none" stroke="var(--white)" stroke-width="3" opacity="0.8"/>
  </svg>
  <h1 class="front__title"><span class="line-1">Frozen</span><span class="line-2">Yoghurt</span></h1>
  <p class="front__tagline">Locker Leichter Genuss<br>100% kalorienarm</p>
  <div class="front__product" role="img" aria-label="Frozen Yoghurt im Becher mit Kirschen und Knuspermüsli, umgeben von Milchspritzern"></div>
  <p class="front__offer">Mit dieser Karte <strong>JETZT GRATIS</strong> testen.</p>
</section>

<section class="card card--back">
  <svg class="back__swoosh" viewBox="0 0 816 576" width="816" height="576" aria-hidden="true">
    <path d="M0 420 C 150 470, 280 540, 420 576 L0 576 Z" fill="var(--green-pale)"/>
    <path d="M0 470 C 140 505, 250 550, 330 576 L0 576 Z" fill="var(--green-light)" opacity="0.5"/>
  </svg>
  <h2 class="back__title"><span class="line-1">Frozen</span><span class="line-2">Yoghurt</span></h2>

  <div class="benefits">
    <p class="benefits__lead">Der gesunde und leichte<br>Sommergenuss</p>
    <ul class="benefits__list">
      <li>nahezu fettrei - nur 2% Fett</li>
      <li>mit der extra Portion Eiweiß<br>und Calcium</li>
      <li>reich an Vitaminen durch eine<br>Vielzahl an Frucht-Toppings</li>
    </ul>
  </div>

  <p class="voucher"><strong>GUTSCHEIN</strong> einlösen und einen<br>Frozen Yoghurt <strong>GRATIS</strong> genießen.</p>

  <div class="divider"></div>

  <div class="brand"><span class="brand__mark"></span>Fresh Corner</div>

  <div class="address">
    <p class="address__intro">Besuchen Sie uns in der...</p>
    <p class="address__line">Linden Eck</p>
    <p class="address__line">Cafebar Fresh Corner</p>
    <p class="address__line">Lindengasse 12-14</p>
    <p class="address__line">3011 Bern</p>
    <p class="address__closing">Wir freuen uns auf Sie!</p>
  </div>
</section>

</body>
</html>
```